New Business Card Design Project

I need a meaningful new business card. Therefore, the website should convey growth, joy, uniqueness, workout and a bit of luxury.
Color scheme should be petrol, gold and matching colors.

```html
<!DOCTYPE html>
<html lang="de">
<head>
<meta charset="utf-8">
<title>Isartal Pilates – Visitenkarte</title>
<link rel="stylesheet" href="https://fonts.googleapis.com/css2?family=Open+Sans:wght@600;700;800&display=swap">
<style>
  :root {
    --stage: #222222;
    --petrol: #17aca0;
    --petrol-deep: #0f7f76;
    --card-dark: #1c1c1c;
    --band-grey: #5b5b5d;
    --white: #ffffff;
  }
  * { box-sizing: border-box; margin: 0; padding: 0; }
  html, body { width: 1200px; height: 780px; overflow: hidden; background: var(--stage); }
  body { font-family: "Open Sans", Arial, sans-serif; position: relative; }

  .card {
    position: absolute; top: 215px; width: 540px; height: 350px;
    border-radius: 22px; overflow: hidden;
  }
  .card--front { left: 40px; background: var(--petrol); }
  .card--back { left: 620px; background: var(--card-dark); border: 4px solid var(--petrol); }

  .front-brand {
    position: absolute; inset: 0; display: flex; align-items: center; justify-content: center; gap: 14px;
    color: var(--petrol-deep); font-weight: 700; font-size: 34px; letter-spacing: 0.5px;
  }
  .brand-dot { width: 22px; height: 22px; border-radius: 50%; background: currentColor; }

  .back-brand {
    position: absolute; left: 30px; top: 110px; width: 220px;
    display: flex; align-items: center; justify-content: center; gap: 10px;
    color: var(--petrol); font-weight: 700; font-size: 24px;
  }
  .back-brand .brand-dot { width: 16px; height: 16px; }

  .divider { position: absolute; left: 268px; top: 60px; width: 3px; height: 160px; background: var(--white); }

  .contact { position: absolute; left: 292px; top: 58px; color: var(--white); }
  .contact__name { color: var(--petrol); font-weight: 800; font-size: 30px; line-height: 1.05; }
  .contact__role { font-weight: 700; font-size: 15px; margin-top: 4px; }
  .contact__list { list-style: none; margin-top: 18px; }
  .contact__list li { display: flex; align-items: center; gap: 10px; font-weight: 600; font-size: 14px; line-height: 24px; }
  .contact__list svg { width: 15px; height: 15px; fill: var(--petrol); flex: none; }

  .social {
    position: absolute; left: 150px; top: 252px; display: flex; align-items: center; gap: 9px;
    color: var(--white); font-weight: 700; font-size: 15px;
  }
  .social__mark { width: 14px; height: 14px; border: 2px solid var(--petrol); border-radius: 4px; }

  .band { position: absolute; left: 0; right: 0; top: 284px; height: 30px; display: flex; }
  .band__petrol { flex: 0 0 52%; background: var(--petrol); }
  .band__grey { flex: 1; background: var(--band-grey); }
</style>
</head>
<body>
  <section class="card card--front" aria-label="Kartenvorderseite">
    <div class="front-brand"><span class="brand-dot"></span>Isartal Pilates</div>
  </section>

  <section class="card card--back" aria-label="Kartenrückseite">
    <div class="back-brand"><span class="brand-dot"></span>Isartal Pilates</div>
    <div class="divider"></div>
    <div class="contact">
      <div class="contact__name">Lena Brückner</div>
      <div class="contact__role">Pilates Studio Trainerin</div>
      <ul class="contact__list">
        <li><svg viewBox="0 0 24 24"><path d="M6.6 10.8a15 15 0 0 0 6.6 6.6l2.2-2.2a1 1 0 0 1 1-.25 11.4 11.4 0 0 0 3.6.57 1 1 0 0 1 1 1V20a1 1 0 0 1-1 1A17 17 0 0 1 3 4a1 1 0 0 1 1-1h3.5a1 1 0 0 1 1 1c0 1.25.2 2.45.57 3.6a1 1 0 0 1-.25 1z"/></svg>+49 170 5550184</li>
        <li><svg viewBox="0 0 24 24"><path d="M3 5h18a1 1 0 0 1 1 1v12a1 1 0 0 1-1 1H3a1 1 0 0 1-1-1V6a1 1 0 0 1 1-1zm1 2.2V17h16V7.2l-8 5.3z"/></svg>hallo@pilates-isartal.de</li>
        <li><svg viewBox="0 0 24 24"><path d="M12 2a10 10 0 1 0 0 20 10 10 0 0 0 0-20zm6.9 6h-3a15 15 0 0 0-1.3-3.9A8 8 0 0 1 18.9 8zM12 4c.8 1.2 1.5 2.5 1.9 4h-3.8c.4-1.5 1.1-2.8 1.9-4zM4.3 14a8 8 0 0 1 0-4h3.4a16 16 0 0 0 0 4zm.8 2h3a15 15 0 0 0 1.3 3.9A8 8 0 0 1 5.1 16zm3-8h-3a8 8 0 0 1 4.3-3.9A15 15 0 0 0 8.1 8zM12 20c-.8-1.2-1.5-2.5-1.9-4h3.8c-.4 1.5-1.1 2.8-1.9 4zm2.3-6H9.7a14 14 0 0 1 0-4h4.6a14 14 0 0 1 0 4zm.3 5.9A15 15 0 0 0 15.9 16h3a8 8 0 0 1-4.3 3.9zM16.3 14a16 16 0 0 0 0-4h3.4a8 8 0 0 1 0 4z"/></svg>www.pilates-isartal.de</li>
      </ul>
    </div>
    <div class="social"><span class="social__mark"></span>isartal_pilatesstudio</div>
    <div class="band"><div class="band__petrol"></div><div class="band__grey"></div></div>
  </section>
</body>
</html>
```